Website for residential builder repair in Australia

I currently have my website setup using Servolink as hosting and started playing around with Wordpress.
I would like this to be able to be imported into Wordpress after built so I can add blog posts and edit site if needed.

I would like a website built that is simple and clear.

the main colours id like for the site are black and white and maybe grey.

I would like a simple welcome page, an about us page, a project page, and a blog page where I can write small articles.

will need to display licence number on website lic. 731046K

Target Market(s)

young to middle age families and couples looking to build a sustainable and high performance house.

Contact Information for Business Card

Tamsel Construction
Lic. 731046K (to be printed small)
email; bram@tamselconstruction.com.au
phone : 0428159067

Bram Keltoy - Director

Number of Pages Required

4 page

Font styles to use
Sans Serif
Other font styles liked:
• match logo

Colors

Designer to choose only greyscale colors for use in the design.

Requirements
Must have
• outline of works

Certified Passive House Tradesperson
New Builds
Renovations
Architectural homes
Nice to have
• thinking dark grey background or black

would like to see the logo embossed to look slightly 3d

back of card to be white or light grey so It can be written on.

letterhead to contain licence number swell

```html
<!DOCTYPE html>
<html lang="en">
<head>
<meta charset="utf-8">
<title>Tamsel Construction</title>
<link rel="stylesheet" href="https://fonts.googleapis.com/css2?family=Jost:wght@400;500;600;700&display=swap">
<style>
:root{
  --ink:#1c1c1c;
  --text:#3a3a3a;
  --muted:#8a8a8a;
  --line:#d8d8d8;
  --dark:#3b3b3b;
  --panel:#4a4a4a;
  --btn:#555555;
  --light:#f1f1f1;
  --white:#ffffff;
  --accent:#b9c94a;
  --blue:#1f5fa0;
  --map:#f3efe6;
}
*{box-sizing:border-box;margin:0;padding:0}
html,body{width:1200px;height:3400px;overflow:hidden}
body{position:relative;font-family:"Jost",sans-serif;color:var(--text);background:var(--white)}
.abs{position:absolute}
/* header */
.site-header{position:absolute;left:0;top:0;width:1200px;height:68px;background:var(--white)}
.brand{position:absolute;left:126px;top:14px;display:flex;align-items:center;gap:8px;font-size:17px;font-weight:600;letter-spacing:3px;color:var(--ink);text-transform:uppercase}
.brand .mark{width:10px;height:10px;background:var(--ink)}
.nav{position:absolute;top:26px;display:flex;font-size:13px;color:var(--ink)}
.nav a{color:inherit;text-decoration:none;position:absolute;white-space:nowrap}
.nav .active{color:var(--muted)}
.quote-btn{position:absolute;left:837px;top:20px;width:98px;height:30px;background:var(--btn);color:#fff;font-size:12px;display:flex;align-items:center;justify-content:center}
.phone{position:absolute;left:955px;top:22px;display:flex;align-items:center;gap:8px;font-size:13px;color:var(--ink);font-weight:500}
.phone .ring{width:24px;height:24px;border:1.5px solid var(--ink);border-radius:50%;display:flex;align-items:center;justify-content:center}
/* hero */
.hero{position:absolute;left:0;top:68px;width:1200px;height:532px;background:linear-gradient(180deg,#3a3c40 0%,#2b2d31 45%,#1f2022 100%)}
.hero h1{position:absolute;top:200px;width:100%;text-align:center;color:#fff;font-size:40px;font-weight:700;letter-spacing:1px}
.hero p{position:absolute;top:258px;left:325px;width:550px;text-align:center;color:#e6e6e6;font-size:14px;line-height:19px}
.btn-light{position:absolute;left:548px;top:325px;width:104px;height:32px;background:#fff;color:var(--ink);font-size:12px;display:flex;align-items:center;justify-content:center}
.dots{position:absolute;left:1156px;top:205px;display:flex;flex-direction:column;gap:10px}
.dots span{width:9px;height:9px;border:1px solid #aaa;border-radius:50%}
.dots span.on{border-color:#fff;background:#fff}
/* section titles */
.sec-title{position:absolute;width:100%;text-align:center;font-size:28px;font-weight:700;color:var(--ink)}
.rule{position:absolute;left:550px;width:100px;height:10px}
.rule::before,.rule::after{content:"";position:absolute;top:5px;width:42px;height:1px;background:#999}
.rule::before{left:0}.rule::after{right:0}
.rule i{position:absolute;left:47px;top:2px;width:6px;height:6px;background:var(--accent)}
/* about */
.about-photo{position:absolute;left:175px;top:670px;width:415px;height:390px;background:linear-gradient(135deg,#c9ccd0 0%,#5d6b78 45%,#28333f 100%)}
.dot-grid{position:absolute;left:152px;top:845px;width:135px;height:240px;background-image:radial-gradient(#c9c9c9 1px,transparent 1.2px);background-size:5px 5px}
.lic{position:absolute;left:463px;top:1010px;width:135px;height:36px;background:rgba(140,140,140,.9);color:#fff;font-size:12px;display:flex;align-items:center;justify-content:center}
.about-text{position:absolute;left:669px;top:700px;width:385px}
.about-text h2{font-size:28px;font-weight:700;color:var(--ink)}
.about-text .lead{margin-top:36px;font-size:14px;line-height:19px;color:var(--ink)}
.about-text p.body{margin-top:22px;font-size:12px;line-height:19px}
.btn-dark{position:absolute;background:var(--btn);color:#fff;font-size:13px;display:flex;align-items:center;justify-content:center}
/* services */
.services{position:absolute;left:0;top:1130px;width:1200px;height:478px;background:var(--dark)}
.services .sec-title{color:#fff}
.svc{position:absolute;top:141px;width:218px;height:266px;background:#fff;border:1px solid #ddd}
.svc .img{height:201px}
.svc .cap{height:65px;display:flex;align-items:center;justify-content:center;text-align:center;font-size:14px;line-height:17px;color:var(--ink);font-weight:500}
.svc.hover{background:var(--panel);border-color:var(--panel)}
.svc.hover .cap{color:#fff}
/* projects */
.projects{position:absolute;left:0;top:1608px;width:1200px;height:509px;background:var(--light)}
.proj{position:absolute;top:140px;width:300px;height:235px}
.proj-card{position:absolute;left:327px;top:163px;width:245px;height:189px;background:#fff;text-align:center}
.proj-card h3{margin-top:14px;font-size:14px;font-weight:700;color:var(--ink)}
.proj-card h3::after{content:"";display:block;width:30px;height:1px;background:var(--ink);margin:6px auto 0}
.proj-card p{margin:18px 22px 0;font-size:12px;line-height:19px}
.proj-card .go{position:absolute;left:82px;bottom:0;width:81px;height:34px;background:var(--dark);display:flex;align-items:center;justify-content:center}
.ctrl{position:absolute;top:412px;height:33px;display:flex;align-items:center;justify-content:center;border:1px solid #999;font-size:13px;color:var(--ink)}
/* blogs */
.blog{position:absolute;top:2256px;width:377px}
.blog .img{height:210px}
.blog .date{position:absolute;left:302px;top:207px;width:67px;height:47px;background:var(--dark);color:#fff;font-size:12px;line-height:15px;text-align:center;padding-top:8px;font-weight:500}
.blog .date b{font-weight:600}
.blog p{margin-top:16px;width:290px;font-size:14px;line-height:18px}
.blog .more{margin-top:16px;font-size:11px;color:var(--ink);display:flex;align-items:center;gap:6px}
/* contact */
.map{position:absolute;left:0;top:2608px;width:1200px;height:405px;background:linear-gradient(120deg,#f4f1ea 0%,#efeadf 60%,#e7eee0 100%)}
.map-label{position:absolute;left:547px;top:2696px;font-size:18px;font-weight:600;letter-spacing:2px;color:#555}
.contact-card{position:absolute;left:213px;top:2774px;width:774px;height:359px;background:#fff;box-shadow:0 4px 18px rgba(0,0,0,.08)}
.contact-card h3{position:absolute;left:34px;top:36px;font-size:19px;font-weight:500;color:var(--blue)}
.field{position:absolute;border:1px solid var(--line);font-size:12px;color:#aaa;padding:10px 12px}
.submit{position:absolute;left:367px;top:287px;width:114px;height:33px;background:var(--dark);color:#fff;font-size:13px;font-weight:500;display:flex;align-items:center;justify-content:center}
.info{position:absolute;left:513px;top:0;width:261px;height:359px;background:var(--panel);color:#fff}
.info h3{position:absolute;left:27px;top:36px;font-size:18px;font-weight:500;color:#fff}
.info-row{position:absolute;left:27px;display:flex;gap:14px}
.info-row small{display:block;font-size:9px;color:#9a9a9a}
.info-row div{font-size:10px;line-height:14px}
.socials{position:absolute;left:30px;top:298px;display:flex;gap:18px}
.socials span{width:23px;height:23px;border-radius:50%;background:#777}
.socials span.on{background:#fff}
/* footer */
.footer-brand{position:absolute;top:3205px;width:100%;text-align:center;font-size:26px;font-weight:600;letter-spacing:5px;color:var(--ink)}
.footer-nav{position:absolute;top:3290px;width:100%;font-size:13px;color:var(--ink)}
.footer-nav a{position:absolute;color:inherit;text-decoration:none;white-space:nowrap}
.copy{position:absolute;top:3322px;width:100%;text-align:center;font-size:10px;color:#888}
</style>
</head>
<body>

<header class="site-header">
  <div class="brand"><span class="mark"></span>Tamsel Construction</div>
  <nav class="nav">
    <a class="active" style="left:403px">Home</a>
    <a style="left:465px">About Us</a>
    <a style="left:545px">Services</a>
    <a style="left:618px">Projects</a>
    <a style="left:689px">Blogs</a>
    <a style="left:746px">Conatct Us</a>
  </nav>
  <div class="quote-btn">Get A Quote</div>
  <div class="phone">
    <span class="ring"><svg width="12" height="12" viewBox="0 0 24 24"><path d="M6.6 10.8a15 15 0 0 0 6.6 6.6l2.2-2.2c.3-.3.7-.4 1-.2 1.1.4 2.3.6 3.6.6.6 0 1 .4 1 1V20c0 .6-.4 1-1 1A17 17 0 0 1 3 4c0-.6.4-1 1-1h3.5c.6 0 1 .4 1 1 0 1.3.2 2.5.6 3.6.1.3 0 .7-.2 1z" fill="#1c1c1c"/></svg></span>
    0428159067
  </div>
</header>

<section class="hero" role="img" aria-label="Photograph of a modern glass office building at dusk">
  <h1>We Build Your Dream</h1>
  <p>Lorem Ipsum is simply dummy text of the printing and typesetting industry. Lorem Ipsum has been the industry's standard dummy text ever since the...</p>
  <div class="btn-light">Read More</div>
  <div class="dots"><span></span><span class="on"></span><span></span></div>
</section>

<section class="about">
  <div class="dot-grid"></div>
  <div class="about-photo" role="img" aria-label="Photograph looking up at a glass skyscraper"></div>
  <div class="lic">Lic. 731046K</div>
  <div class="about-text">
    <h2>About Us</h2>
    <div class="rule" style="left:0;top:40px"><i></i></div>
    <p class="lead">Lorem Ipsum is simply dummy text of the printing and typesetting industry.</p>
    <p class="body">Lorem Ipsum is simply dummy text of the printing and typeset-ting industry. Lorem Ipsum has been the industry's standard dummy text ever since the 1500s.</p>
    <p class="body">when an unknown printer took a galley of type and scrambled it to make a type specimen book. It has survived not only five centuries, but also the leap into...</p>
  </div>
  <div class="btn-dark" style="left:669px;top:998px;width:121px;height:32px">Read More</div>
</section>

<section class="services">
  <h2 class="sec-title" style="top:56px">Services</h2>
  <div class="rule" style="top:96px"><i></i></div>
  <div class="svc" style="left:133px"><div class="img" role="img" aria-label="Tradesperson sealing a wall joint" style="background:linear-gradient(135deg,#d7d7d2,#6e7a84 60%,#2d3137)"></div><div class="cap">Certified Passive<br>House Tradesperson</div></div>
  <div class="svc hover" style="left:372px"><div class="img" role="img" aria-label="House frame with red roof tiles under construction" style="background:linear-gradient(160deg,#c9cfd6,#b8573d 55%,#7a3a2a)"></div><div class="cap">New Builds</div></div>
  <div class="svc" style="left:610px"><div class="img" role="img" aria-label="Room shown before and after renovation" style="background:linear-gradient(90deg,#d9d6d0 0%,#bfb9ae 50%,#e9d9c2 60%,#c7a278 100%)"></div><div class="cap">Renovations</div></div>
  <div class="svc" style="left:849px"><div class="img" role="img" aria-label="Modern architectural home at twilight" style="background:linear-gradient(180deg,#4f6d94 0%,#6d7f8e 50%,#c99a64 70%,#3c5a2e 100%)"></div><div class="cap">Architectural Homes</div></div>
</section>

<section class="projects">
  <h2 class="sec-title" style="top:56px">Projects</h2>
  <div class="rule" style="top:95px"><i></i></div>
  <div class="proj" style="left:0" role="img" aria-label="Apartment towers against blue sky" style="background:#7f9bbd"><div style="width:100%;height:100%;background:linear-gradient(135deg,#a9bcd4,#5f7ea6 60%,#c9b77a)"></div></div>
  <div class="proj" style="left:300px" role="img" aria-label="Building site with crane"><div style="width:100%;height:100%;background:linear-gradient(180deg,#5a5c60,#3b3d40)"></div></div>
  <div class="proj" style="left:600px" role="img" aria-label="High-rise apartment block"><div style="width:100%;height:100%;background:linear-gradient(160deg,#7e98bf,#3d4d64 60%,#8893a0)"></div></div>
  <div class="proj" style="left:900px" role="img" aria-label="Modern apartment building with balconies"><div style="width:100%;height:100%;background:linear-gradient(135deg,#3f7fb8,#213a4f 45%,#c18d6a 70%,#e6e1da)"></div></div>
  <div class="proj-card">
    <h3>Lorem Ipsum</h3>
    <p>Lorem Ipsum is simply dummy text of the printing and typeset-ting industry...</p>
    <div class="go"><svg width="20" height="12" viewBox="0 0 20 12"><path d="M1 6h17M13 1l5 5-5 5" stroke="#fff" stroke-width="1.5" fill="none"/></svg></div>
  </div>
  <div class="ctrl" style="left:492px;width:45px;border-color:#bbb"><svg width="18" height="10" viewBox="0 0 18 10"><path d="M17 5H2M6 1L2 5l4 4" stroke="#777" stroke-width="1.3" fill="none"/></svg></div>
  <div class="ctrl" style="left:543px;width:45px;background:var(--dark);border-color:var(--dark)"><svg width="18" height="10" viewBox="0 0 18 10"><path d="M1 5h15M12 1l4 4-4 4" stroke="#fff" stroke-width="1.3" fill="none"/></svg></div>
  <div class="ctrl" style="left:601px;width:107px;border-color:#444">View All</div>
</section>

<h2 class="sec-title" style="top:2182px">Blogs</h2>
<div class="rule" style="top:2220px"><i></i></div>
<article class="blog" style="left:213px">
  <div class="img" role="img" aria-label="Apartment tower seen from below" style="background:linear-gradient(150deg,#7f9dc8,#3a4a62 55%,#9aa3ad)"></div>
  <div class="date">25 Oct<br><b>2020</b></div>
  <p>Lorem Ipsum is simply dummy text of the printing and typesetting industry.</p>
  <div class="more"><svg width="9" height="8" viewBox="0 0 9 8"><path d="M0 4h8M5 1l3 3-3 3" stroke="#1c1c1c" fill="none"/></svg>Read More</div>
</article>
<article class="blog" style="left:610px">
  <div class="img" role="img" aria-label="Bright living room with armchairs and fireplace" style="background:linear-gradient(120deg,#e7e2d8,#b49d7f 50%,#d8d3c9)"></div>
  <div class="date">26 Oct<br><b>2020</b></div>
  <p>Lorem Ipsum is simply dummy text of the printing and typesetting industry.</p>
  <div class="more"><svg width="9" height="8" viewBox="0 0 9 8"><path d="M0 4h8M5 1l3 3-3 3" stroke="#1c1c1c" fill="none"/></svg>Read More</div>
</article>

<div class="map" role="img" aria-label="Map of central Australia"></div>
<div class="map-label">Australia</div>

<section class="contact-card">
  <h3>Let's Get Started</h3>
  <div class="field" style="left:34px;top:81px;width:216px;height:36px">Name</div>
  <div class="field" style="left:265px;top:81px;width:216px;height:36px">Email</div>
  <div class="field" style="left:34px;top:132px;width:216px;height:36px">Phone</div>
  <div class="field" style="left:265px;top:132px;width:216px;height:36px">What are you looking for?
    <svg style="position:absolute;right:10px;top:15px" width="8" height="5" viewBox="0 0 8 5"><path d="M0 0h8L4 5z" fill="#333"/></svg></div>
  <div class="field" style="left:34px;top:182px;width:447px;height:92px">Message</div>
  <div class="submit">Submit</div>
  <div class="info">
    <h3>Contact Info</h3>
    <div class="info-row" style="top:80px">
      <svg width="14" height="18" viewBox="0 0 14 18"><path d="M7 0a7 7 0 0 0-7 7c0 5 7 11 7 11s7-6 7-11a7 7 0 0 0-7-7zm0 10a3 3 0 1 1 0-6 3 3 0 0 1 0 6z" fill="#bbb"/></svg>
      <div><small>Location</small>Tamsel Construction<br>12 / 8 Corran Street<br>HARBOUR VALE QLD 4870<br>AUSTRALIA</div>
    </div>
    <div class="info-row" style="top:170px">
      <svg width="14" height="14" viewBox="0 0 24 24"><path d="M6.6 10.8a15 15 0 0 0 6.6 6.6l2.2-2.2c.3-.3.7-.4 1-.2 1.1.4 2.3.6 3.6.6.6 0 1 .4 1 1V20c0 .6-.4 1-1 1A17 17 0 0 1 3 4c0-.6.4-1 1-1h3.5c.6 0 1 .4 1 1 0 1.3.2 2.5.6 3.6.1.3 0 .7-.2 1z" fill="#bbb"/></svg>
      <div><small>Call Us</small>0428159067</div>
    </div>
    <div class="info-row" style="top:214px">
      <svg width="16" height="12" viewBox="0 0 16 12"><rect x=".5" y=".5" width="15" height="11" fill="none" stroke="#bbb"/><path d="M.5.5 8 7l7.5-6.5" fill="none" stroke="#bbb"/></svg>
      <div><small>Email</small>bram@tamselconstruction.com.au</div>
    </div>
    <div class="socials"><span></span><span class="on"></span><span></span><span></span></div>
  </div>
</section>

<footer>
  <div class="footer-brand">TAMSEL CONSTRUCTION</div>
  <nav class="footer-nav">
    <a style="left:343px;color:#bbb">Home</a>
    <a style="left:424px">About Us</a>
    <a style="left:525px">Services</a>
    <a style="left:618px">Projects</a>
    <a style="left:709px">Blogs</a>
    <a style="left:785px">Contact Us</a>
  </nav>
  <div class="copy">Copyright © 2020 Tamsel Construction. All Rights Reserved</div>
</footer>

</body>
</html>
```